Estate Planner needs an Ad for a local newsletter

I need an ad designed for my practice as an estate planning attorney. The ad will be in a newsletter that targets individuals over the age of 55. My ad is 7.5"W x 4.6"H (a half page ad) .
The wording should include:
(No subject)
Whitcombe, Dana

Dana Whitcombe

Wisdom Meets Planning
Your Estate, Your Legacy

After 23 years as a military spouse, moving our family of six across the country,
I learned the true value of careful planning. Today I help Brevard County's seniors protect what matters most – their family’s future and their life’s work.

I understand that your estate is more than just assets – it's a lifetime of wise
decisions, cherished memories, and dreams for your family's future.

Professional Estate Planning:
• Wills & Living Trusts • Healthcare Directives
• Power of Attorney • Asset Protection
• Probate Avoidance • Peace of Mind

Plus also needs to have my contact information:
PRV Law
Dana Whitcombe
Attorney/Of Counsel
4630 Oakhollow Road
Melbourne, Florida 32901
(555) 814-0962
dwhitcombe@prvlawgroup.example
Logo is attached.

```html
<!DOCTYPE html>
<html lang="en">
<head>
<meta charset="utf-8">
<title>PRV Law – Dana Whitcombe Estate Planning Ad</title>
<link rel="stylesheet" href="https://fonts.googleapis.com/css2?family=Poppins:wght@400;500;600&family=Libre+Baskerville:wght@700&display=swap">
<style>
  :root {
    --navy: #16213f;
    --navy-band: #12264a;
    --red: #c2143a;
    --sky-top: #a9dcf3;
    --sky-mid: #d7d9ee;
    --water: #b9e0f4;
    --white: #ffffff;
    --rule: #6a7390;
    --page: #3f3f3f;
  }
  * { box-sizing: border-box; margin: 0; padding: 0; }
  html, body { width: 1200px; height: 859px; overflow: hidden; background: var(--page); }
  body { font-family: "Poppins", sans-serif; color: var(--navy); }

  .ad {
    position: absolute; left: 0; top: 62px;
    width: 1200px; height: 735px;
    background: linear-gradient(180deg, var(--sky-top) 0%, var(--sky-mid) 40%, var(--water) 52%, #dff0fa 68%, var(--white) 86%);
    overflow: hidden;
  }
  .skyline {
    position: absolute; left: 0; top: 192px; width: 1200px; height: 165px;
    background: linear-gradient(180deg, rgba(190,190,225,0) 0%, #a8a6cf 25%, #7f7fae 60%, #9fb6d6 88%, rgba(185,224,244,0) 100%);
  }

  .brand { position: absolute; left: 0; top: 22px; width: 1200px; text-align: center; }
  .brand-name { font-weight: 600; font-size: 80px; line-height: 1; color: var(--navy); }
  .brand-partners { position: absolute; left: 0; top: 112px; width: 1200px; font-weight: 500; font-size: 17px; line-height: 22px; }
  .brand-est { position: absolute; left: 0; top: 143px; width: 1200px; font-family: "Libre Baskerville", serif; font-weight: 700; font-size: 16px; line-height: 22px; }

  .attorney-name { position: absolute; left: 39px; top: 371px; font-weight: 500; font-size: 46px; line-height: 54px; white-space: nowrap; }
  .attorney-title { position: absolute; left: 42px; top: 426px; font-weight: 500; font-size: 21px; line-height: 26px; color: var(--red); letter-spacing: .3px; white-space: nowrap; }

  .bio { position: absolute; left: 41px; top: 474px; width: 536px; font-size: 16.4px; line-height: 21.5px; text-align: justify; }
  .bio p + p { margin-top: 22px; }

  .divider-v { position: absolute; left: 600px; top: 476px; height: 166px; border-left: 1.5px dotted var(--rule); }

  .tagline-main { position: absolute; left: 600px; top: 371px; width: 580px; text-align: center; font-weight: 500; font-size: 42px; line-height: 54px; white-space: nowrap; }
  .tagline-sub { position: absolute; left: 600px; top: 425px; width: 580px; text-align: center; font-weight: 500; font-size: 20px; line-height: 26px; color: var(--red); white-space: nowrap; }

  .services-title { position: absolute; left: 620px; top: 470px; font-weight: 600; font-size: 30.5px; line-height: 38px; letter-spacing: .2px; white-space: nowrap; }

  .services { list-style: none; position: absolute; left: 616px; top: 514px; width: 550px; display: grid; grid-template-columns: 186px 194px 170px; grid-template-rows: 62px 70px; }
  .service { display: flex; align-items: center; gap: 6px; padding: 0 6px 0 4px; position: relative; }
  .service:nth-child(-n+3)::before { content: ""; position: absolute; left: 0; right: 10px; bottom: 0; border-bottom: 1.5px dotted var(--rule); }
  .service:nth-child(n+4) { padding-top: 6px; }
  .service:not(:nth-child(3n))::after { content: ""; position: absolute; right: 0; top: 4px; bottom: 4px; border-right: 1.5px dotted var(--rule); }
  .service svg { flex: 0 0 30px; width: 30px; height: 30px; }
  .service-label { flex: 1; text-align: center; font-size: 18px; line-height: 21px; white-space: nowrap; }

  .contact-band { position: absolute; left: 0; top: 664px; width: 1200px; height: 71px; background: var(--navy-band); color: var(--white); }
  .contact-item { position: absolute; top: 0; height: 71px; display: flex; align-items: center; gap: 12px; font-size: 16.2px; line-height: 20px; white-space: nowrap; }
  .contact-item svg { width: 24px; height: 24px; flex: 0 0 24px; }
  .contact-address { left: 32px; gap: 16px; }
  .contact-email { left: 318px; gap: 14px; }
  .contact-web { left: 664px; gap: 16px; }
  .contact-phone { left: 900px; gap: 13px; font-weight: 600; font-size: 28px; }
</style>
</head>
<body>
  <main class="ad">
    <div class="skyline" role="img" aria-label="City skyline at dusk across the water with a suspension bridge"></div>

    <header class="brand">
      <div class="brand-name">PRV Law</div>
    </header>
    <div class="brand-partners" style="text-align:center">Pemberton · Reyes · Vance · Holloway · Aldana</div>
    <div class="brand-est" style="text-align:center">EST.1976</div>

    <h1 class="attorney-name">Dana Whitcombe</h1>
    <div class="attorney-title">ATTORNEY/OF COUNSEL</div>

    <section class="bio">
      <p>After 23 years as a military spouse, moving our family of six across the country. I learned the true value of careful planning. Today I help Brevard County's seniors protect what matters most – their family’s future and their life’s work.</p>
      <p>I understand that your estate is more than just assets – it's a lifetime of wise decisions, cherished memories, and dreams for your family's future.</p>
    </section>

    <div class="divider-v"></div>

    <h2 class="tagline-main">Wisdom Meets Planning</h2>
    <div class="tagline-sub">YOUR ESTATE, YOUR LEGACY</div>

    <h3 class="services-title">PROFESSIONAL ESTATE PLANNING:</h3>
    <ul class="services">
      <li class="service">
        <svg viewBox="0 0 30 30" fill="none" stroke="var(--red)" stroke-width="2" stroke-linejoin="round"><path d="M4 8v19h16v-5"/><path d="M9 23c2-9 8-17 17-20-1 8-7 15-15 18z"/><path d="M9 23l8-11"/></svg>
        <span class="service-label">Wills &amp; Living<br>Trusts</span>
      </li>
      <li class="service">
        <svg viewBox="0 0 30 30" fill="none" stroke="var(--red)" stroke-width="2.2" stroke-linejoin="round"><path d="M15 26C6 19 3 15 3 10.5A6 6 0 0 1 15 8a6 6 0 0 1 12 2.5C27 15 24 19 15 26z"/></svg>
        <span class="service-label">Healthcare<br>Directives</span>
      </li>
      <li class="service">
        <svg viewBox="0 0 30 30" fill="none" stroke="var(--red)" stroke-width="1.8" stroke-linejoin="round"><path d="M3 6h14M3 6v22h16v-4"/><path d="M18 4v18M11 8h14M11 8l-3 8h6zM25 8l-3 8h6z"/></svg>
        <span class="service-label">Power of<br>Attorney</span>
      </li>
      <li class="service">
        <svg viewBox="0 0 30 30" fill="none" stroke="var(--red)" stroke-width="2" stroke-linejoin="round"><path d="M15 2l11 4v8c0 7-5 11-11 14C9 25 4 21 4 14V6z"/><text x="15" y="20" text-anchor="middle" font-family="Poppins, sans-serif" font-size="13" font-weight="600" fill="var(--red)" stroke="none">$</text></svg>
        <span class="service-label">Asset<br>Protection</span>
      </li>
      <li class="service">
        <svg viewBox="0 0 30 30" fill="none" stroke="var(--red)" stroke-width="2" stroke-linejoin="round"><path d="M20 4H5v24h17V14"/><path d="M9 12h8M9 17h9M9 22h9"/><path d="M24 2l1.3 3 3.2.2-2.5 2 .8 3.1-2.8-1.7-2.8 1.7.8-3.1-2.5-2 3.2-.2z" stroke-width="1.4"/></svg>
        <span class="service-label">Probate<br>Avoidance</span>
      </li>
      <li class="service">
        <svg viewBox="0 0 30 30" fill="none" stroke="var(--red)" stroke-width="2.2"><circle cx="15" cy="15" r="12"/><path d="M15 3v24M15 15l-8.5 8.5M15 15l8.5 8.5"/></svg>
        <span class="service-label">Peace of<br>Mind</span>
      </li>
    </ul>

    <footer class="contact-band">
      <div class="contact-item contact-address">
        <svg viewBox="0 0 24 24"><circle cx="12" cy="12" r="12" fill="var(--red)"/><path d="M12 5a4.5 4.5 0 0 0-4.5 4.5C7.5 13 12 18 12 18s4.5-5 4.5-8.5A4.5 4.5 0 0 0 12 5z" fill="var(--navy-band)"/><circle cx="12" cy="9.5" r="1.6" fill="var(--red)"/></svg>
        <span>4630 Oakhollow Road<br>Melbourne, Florida 32901</span>
      </div>
      <div class="contact-item contact-email">
        <svg viewBox="0 0 24 24"><circle cx="12" cy="12" r="12" fill="var(--red)"/><rect x="6" y="8" width="12" height="8.5" rx="1" fill="var(--navy-band)"/><path d="M6.5 8.5l5.5 4.5 5.5-4.5" fill="none" stroke="var(--red)" stroke-width="1.2"/></svg>
        <span>dwhitcombe@prvlawgroup.example</span>
      </div>
      <div class="contact-item contact-web">
        <svg viewBox="0 0 24 24"><circle cx="12" cy="12" r="11.5" fill="var(--red)"/><path d="M2 12h20M12 .5c-4 4-4 19 0 23M12 .5c4 4 4 19 0 23" fill="none" stroke="var(--navy-band)" stroke-width="1.3"/></svg>
        <span>prvlawgroup.example</span>
      </div>
      <div class="contact-item contact-phone">
        <svg viewBox="0 0 24 24"><circle cx="12" cy="12" r="12" fill="var(--red)"/><path d="M8.5 6.5l2 .3.8 3-1.5 1.2a9 9 0 0 0 3.4 3.4l1.2-1.5 3 .8.3 2c-.3 1-1.3 1.8-2.4 1.6C10.6 16.5 7.5 13.4 6.9 8.9c-.2-1.1.6-2.1 1.6-2.4z" fill="var(--navy-band)"/></svg>
        <span>(555) 814-0962</span>
      </div>
    </footer>
  </main>
</body>
</html>
```